Orvek Electric Construction Power Runs Deep!

We have an up coming meeting with a developer and general contractor. This card must bring out the best in my business. My business is an up and coming MDBE certified electrical contactor. I need a very powerful card to represent me business that we be bold and represent what I am about. POWER RUNS DEEP!

Target Market(s)

General Contractors, developers and property owners

Industry/Entity Type

Electrical

Contact Information for Business Card

great card that really brings out my bussiness

Colors
0355a3
3276b5
0393ce
34a6d7

Requirements
Must have
• Great design
Nice to have
• very different and noticeable card
Should not have
• open to anything

```html
<!DOCTYPE html>
<html lang="en">
<head>
<meta charset="utf-8">
<title>Orvek Electric Construction – Business Card</title>
<link href="https://fonts.googleapis.com/css2?family=Arimo:wght@400;700&family=Open+Sans:wght@400;700&display=swap" rel="stylesheet">
<style>
  :root{
    --navy:#1b4580;
    --deep:#0355a3;
    --mid:#3276b5;
    --bright:#0393ce;
    --sky:#34a6d7;
    --stage:#000;
    --paper-1:#c9cacc;
    --paper-2:#ececed;
    --white:#fff;
  }
  *{margin:0;padding:0;box-sizing:border-box}
  html,body{width:1200px;height:1000px;overflow:hidden;background:var(--stage)}
  .canvas{position:relative;width:1200px;height:1000px}
  .card{position:absolute;left:258px;width:683px;height:390px;overflow:hidden}
  .card-front{
    top:96px;
    background:linear-gradient(180deg,#1a4a84 0%,#0b87c9 30%,#0a94d4 50%,#0b86c8 70%,#1a4a84 100%);
  }
  .card-back{
    top:516px;
    background:radial-gradient(ellipse at 60% 55%,var(--paper-2) 0%,#dcdddf 45%,var(--paper-1) 100%);
  }
  .brand-mark{position:absolute;display:flex;align-items:center;gap:10px;
    font-family:"Arimo",Arial,sans-serif;font-weight:700;color:var(--navy)}
  .brand-mark .dot{width:22px;height:22px;background:var(--navy)}
  .front-mark{left:0;right:0;top:120px;justify-content:center;font-size:40px}
  .front-name{position:absolute;left:0;right:0;top:221px;text-align:center;
    font-family:"Arimo",Arial,sans-serif;font-size:28px;color:var(--white);
    text-shadow:0 1px 2px rgba(0,0,0,.35)}
  .front-tagline{position:absolute;left:0;right:0;top:255px;text-align:center;
    font-family:"Open Sans",Arial,sans-serif;font-weight:700;font-size:13px;color:var(--navy);
    text-shadow:0 1px 1px rgba(0,0,0,.25)}
  .back-mark{left:124px;top:66px;font-size:36px}
  .back-name{position:absolute;left:27px;top:153px;
    font-family:"Arimo",Arial,sans-serif;font-size:27px;color:var(--bright)}
  .back-tagline{position:absolute;left:27px;top:185px;
    font-family:"Open Sans",Arial,sans-serif;font-weight:700;font-size:13px;color:var(--navy)}
  .person{position:absolute;right:28px;top:48px;text-align:right;font-family:"Open Sans",Arial,sans-serif}
  .person-name{font-size:25px;line-height:28px;color:var(--navy);letter-spacing:.5px}
  .person-name b{font-weight:700}
  .person-title{font-size:20px;line-height:24px;color:var(--bright)}
  .person-bar{position:absolute;right:0;top:50px;width:17px;height:45px;background:var(--bright)}
  .side-bar{position:absolute;left:0;top:236px;width:14px;height:154px;background:var(--navy)}
  .contacts{position:absolute;left:28px;top:236px;list-style:none;
    font-family:"Open Sans",Arial,sans-serif;font-size:20px;color:var(--navy)}
  .contacts li{display:flex;align-items:center;gap:14px;height:22px}
  .contacts svg{width:20px;height:18px;fill:var(--navy)}
  .address{position:absolute;left:29px;top:313px;
    font-family:"Open Sans",Arial,sans-serif;font-size:20px;line-height:24px;color:var(--navy)}
  .faint-mark{position:absolute;left:380px;top:129px;width:288px;height:245px;
    background:radial-gradient(circle at 50% 55%,rgba(255,255,255,.55),rgba(200,201,204,.15) 70%);
    border-radius:8px}
</style>
</head>
<body>
<main class="canvas">
  <section class="card card-front">
    <div class="brand-mark front-mark"><span class="dot"></span>Orvek</div>
    <h1 class="front-name">Orvek Electric Construction</h1>
    <p class="front-tagline">Certified DBE &amp; MWBE Electrical Contractor</p>
  </section>

  <section class="card card-back">
    <div class="brand-mark back-mark"><span class="dot"></span>Orvek</div>
    <h2 class="back-name">Orvek Electric Construction</h2>
    <p class="back-tagline">Certified DBE &amp; MWBE Electrical Contractor</p>

    <div class="person">
      <p class="person-name">YOUR <b>NAME</b></p>
      <p class="person-title">Title</p>
    </div>
    <div class="person-bar"></div>

    <div class="faint-mark" role="img" aria-label="Faint embossed brand decoration"></div>

    <div class="side-bar"></div>
    <ul class="contacts">
      <li><svg viewBox="0 0 20 18"><path d="M2 6c0-3 4-4 8-4s8 1 8 4l-3 1-1-2H6L5 7zM5 8h10l3 8H2z"/><circle cx="10" cy="12" r="2.2" fill="#d9dadc"/></svg>123-456-7890</li>
      <li><svg viewBox="0 0 20 18"><rect x="1" y="3" width="18" height="12"/><path d="M1 3l9 7 9-7" fill="none" stroke="#d9dadc" stroke-width="1.6"/></svg>yourname@orvekec.com</li>
      <li><svg viewBox="0 0 20 18"><circle cx="10" cy="9" r="8"/><path d="M6 5c2 1 1 3 3 3s1 3 3 4M12 3c0 2 2 2 3 4" fill="none" stroke="#d9dadc" stroke-width="1.4"/></svg>www.orvekec.com</li>
    </ul>
    <p class="address">company address, company address<br>company address</p>
  </section>
</main>
</body>
</html>
```